Create a 2-sided postcard design (standard size) for Torlen Systems, a professional low-voltage and security integration company.
Side 1 – Front (Marketing Side)
Headline / Intro:
"Torlen Systems – Security, Connectivity, and Peace of Mind."
Brief Overview / Summary:
Torlen Systems provides complete security and technology integration solutions for commercial, industrial, and multifamily properties. From access control to fire systems, we specialize in delivering seamless, scalable, and reliable installations supported by professional service and ongoing care.
Services Breakdown:
Access Control – Cloud-based and enterprise access solutions to manage entry and permissions.
CCTV / Video Surveillance – Protect your property with high-definition cameras and remote monitoring.
Intrusion Alarm – Professional-grade systems to detect and deter unauthorized access.
Audio-Visual – From conference rooms to distributed audio and digital displays.
Fire Systems – Code-compliant alarm systems with 24/7 QX monitoring and life-safety support.
Structured Data Cabling – Low-voltage and fiber cabling for reliable network infrastructure.
Trusted By (Logos):
Moro, Velpurna, Gildpath, Carrow Investments, Bolt Hardware, Quillfen Games, Ledger Stewardship Partners, KEYframe
Technology partners:
Include logos of brands like Tamzo, Rook Lantern Networks, JMW , Digital Sentrel, Polmira, RTN, Blazeron
Contact Info:
📧 sales@torlensystems.example
📞 555-014-2739
🌐 torlensystems.example
🖼️ Side 2 – Back (Branding Side)
Primary Focus:
Large, centered Torlen Systems logo.
Subtext / Tagline (Optional):
“Your Security and Technology Partner.”
List of Services (Under Logo):
Access Control | CCTV | Intrusion Alarm | Audio-Visual | Fire | Data
🎨 Design Preferences:
Clean, modern, and professional layout.
Corporate tones (e.g., black and white, bold accents).
Use clean typography and icons for service areas.
Logo should be prominent on the back and represent the brand with strength and clarity.
Open to designer layout and creative interpretation as long as it stays on brand.
Industry/Entity Type
Commercial Security
Colors
Designer to choose only greyscale colors for use in the design.
Look and feel
Each slider illustrates characteristics of the customer's brand and the style your logo design should communicate.

```html
<!DOCTYPE html>
<html lang="en">
<head>
<meta charset="utf-8">
<title>Torlen Systems Postcard</title>
<link href="https://fonts.googleapis.com/css2?family=Montserrat:wght@600;700&family=Roboto:wght@400;500;700;900&display=swap" rel="stylesheet">
<style>
:root{
  --stage:#a8a3a3;
  --ink:#111111;
  --paper:#ffffff;
  --muted:#2b2b2b;
  --line:#c9c9c9;
  --soft:#efefef;
}
*{margin:0;padding:0;box-sizing:border-box}
html,body{width:970px;height:1200px;overflow:hidden}
body{background:var(--stage);font-family:"Roboto",sans-serif;color:var(--ink);position:relative}
.card{position:absolute;left:81px;width:809px;height:519px;background:var(--paper);overflow:hidden;box-shadow:0 6px 24px rgba(0,0,0,.35)}
.card-front{top:65px}
.card-back{top:616px}

/* front: dark panel */
.intro-panel{position:absolute;left:0;top:0;width:364px;height:519px;background:var(--ink);
  clip-path:polygon(0 0,364px 0,364px 470px,134px 470px,77px 519px,0 519px);color:var(--paper)}
.intro-art{position:absolute;left:0;top:330px;width:364px;height:140px;
  background:radial-gradient(ellipse at 50% 55%,#4a4a4a 0%,#262626 45%,#111 80%)}
.brand-word{position:absolute;left:43px;top:46px;font-family:"Montserrat",sans-serif;font-weight:600;line-height:1}
.brand-word .name{display:block;font-size:34px;letter-spacing:.5px}
.brand-word .sub{display:block;font-size:18px;letter-spacing:5px;margin-top:5px}
.headline{position:absolute;left:43px;top:122px;width:300px;font-family:"Montserrat",sans-serif;font-weight:700;font-size:23px;line-height:35px}
.summary{position:absolute;left:43px;top:205px;width:277px;font-size:13.4px;line-height:20.5px;text-align:justify}

/* front: services */
.service{position:absolute;width:116px}
.service h3{font-weight:500;font-size:12.3px;line-height:15px;margin-bottom:7px}
.service p{font-size:8.9px;line-height:13.7px;color:var(--muted)}
.icon-pair{position:absolute;left:523px;width:110px;height:64px}

.group-title{position:absolute;left:400px;font-weight:500;font-size:14.5px}
.logo-row{position:absolute;left:400px;display:flex;gap:4px}
.logo-chip{width:45px;height:25px;border:1px solid var(--line);border-radius:2px;display:flex;align-items:center;justify-content:center;
  font-size:6.2px;font-weight:500;color:var(--muted);text-align:center;line-height:1.05;padding:0 2px}

.contact{position:absolute;top:480px;display:flex;align-items:center;gap:7px;font-size:14px;color:var(--ink);white-space:nowrap}
.contact svg{width:30px;height:30px;flex:none}

/* back */
.back-texture{position:absolute;inset:0;background:linear-gradient(170deg,#fafafa 0%,#f1f1f1 40%,#e2e2e2 70%,#f6f6f6 100%)}
.back-brand{position:absolute;left:0;right:0;top:36px;text-align:center;font-family:"Montserrat",sans-serif;font-weight:700;line-height:1}
.back-brand .name{display:block;font-size:70px;letter-spacing:1px}
.back-brand .sub{display:block;font-size:33px;letter-spacing:14px;margin-top:8px;padding-left:14px}
.service-list{position:absolute;left:0;right:0;top:180px;text-align:center;font-weight:500;font-size:16.6px}
.tagline-band{position:absolute;left:0;top:234px;width:809px;height:124px;background:var(--ink);color:var(--paper);
  display:flex;align-items:center;justify-content:center;text-align:center}
.tagline-band h2{font-weight:900;font-size:42px;line-height:48px}
.address-box{position:absolute;left:518px;top:383px;width:270px;height:111px;border:1px solid var(--line);background:rgba(255,255,255,.35);
  padding:22px 0 0 30px;font-size:11px}
</style>
</head>
<body>

<section class="card card-front">
  <div class="intro-panel">
    <div class="intro-art" role="img" aria-label="Dark illustration of a padlock shield linked by circuit lines to security icons"></div>
    <div class="brand-word"><span class="name">TORLEN</span><span class="sub">SYSTEMS</span></div>
    <h1 class="headline">Security, Connectivity, and Peace of Mind.</h1>
    <p class="summary">Torlen Systems provides complete security and technology integration solutions for commercial, industrial, and multifamily properties. From access control to fire systems, we specialize in delivering seamless, scalable, and reliable installations supported by professional service and ongoing care.</p>
  </div>

  <div class="service" style="left:403px;top:40px"><h3>Access Control</h3><p>Cloud-based and enterprise access solutions to manage entry and permissions.</p></div>
  <div class="service" style="left:645px;top:40px;width:140px"><h3>CCTV / Video<br>Surveillance</h3><p>Protect your property with high-definition cameras and remote monitoring.</p></div>
  <div class="service" style="left:400px;top:127px"><h3>Intrusion Alarm</h3><p>Professional-grade systems to detect and deter unauthorized access.</p></div>
  <div class="service" style="left:645px;top:127px;width:140px"><h3>Audio-Visual</h3><p>From conference rooms to distributed audio and digital displays.</p></div>
  <div class="service" style="left:400px;top:210px"><h3>Fire Systems</h3><p>Code-compliant alarm systems with 24/7 QX monitoring and life-safety support.</p></div>
  <div class="service" style="left:645px;top:210px;width:140px"><h3>Structured Data Cabling</h3><p>Low-voltage and fiber cabling for reliable network infrastructure.</p></div>

  <svg class="icon-pair" style="top:46px" viewBox="0 0 110 64" fill="none" stroke="#111" stroke-width="1.6">
    <path d="M32 2 62 32 32 62 2 32Z"/><path d="M78 2 108 32 78 62 48 32Z"/>
    <circle cx="32" cy="27" r="5"/><path d="M24 38h16M32 32v6"/>
    <rect x="70" y="25" width="14" height="9" rx="1"/><path d="M84 28l5-2v8l-5-2M76 34v6"/>
  </svg>
  <svg class="icon-pair" style="top:134px" viewBox="0 0 110 64" fill="none" stroke="#111" stroke-width="1.6">
    <path d="M32 2 62 32 32 62 2 32Z"/><path d="M78 2 108 32 78 62 48 32Z"/>
    <path d="M32 22l8 14H24Z"/><path d="M32 27v4"/>
    <path d="M70 36v-5a8 8 0 0 1 16 0v5"/><rect x="68" y="33" width="4" height="6"/><rect x="84" y="33" width="4" height="6"/>
  </svg>
  <svg class="icon-pair" style="top:217px" viewBox="0 0 110 64" fill="none" stroke="#111" stroke-width="1.6">
    <path d="M32 2 62 32 32 62 2 32Z"/><path d="M78 2 108 32 78 62 48 32Z"/>
    <path d="M32 22c5 5 6 9 6 12a6 6 0 0 1-12 0c0-3 1-7 6-12Z"/>
    <rect x="72" y="22" width="7" height="10"/><path d="M75.5 32v8c0 3 8 3 8 0v-10"/>
  </svg>

  <h2 class="group-title" style="top:311px">Trusted By</h2>
  <div class="logo-row" style="top:344px">
    <div class="logo-chip">Moro</div>
    <div class="logo-chip">Velpurna</div>
    <div class="logo-chip">Gildpath</div>
    <div class="logo-chip">Carrow Investments</div>
    <div class="logo-chip">Bolt Hardware</div>
    <div class="logo-chip">Quillfen Games</div>
    <div class="logo-chip">Ledger Stewardship</div>
    <div class="logo-chip">KEYframe</div>
  </div>

  <h2 class="group-title" style="top:388px">Technology Partners</h2>
  <div class="logo-row" style="top:421px">
    <div class="logo-chip">Tamzo</div>
    <div class="logo-chip">Rook Lantern</div>
    <div class="logo-chip">JMW</div>
    <div class="logo-chip">Digital Sentrel</div>
    <div class="logo-chip">Polmira</div>
    <div class="logo-chip">RTN</div>
    <div class="logo-chip">Blazeron</div>
  </div>

  <div class="contact" style="left:150px">
    <svg viewBox="0 0 32 32"><path d="M16 0 32 16 16 32 0 16Z" fill="#111"/><rect x="10.5" y="12" width="11" height="8" fill="#fff"/><path d="M10.5 12l5.5 4.5 5.5-4.5" fill="none" stroke="#111" stroke-width="1"/></svg>
    <span>sales@torlensystems.example</span>
  </div>
  <div class="contact" style="left:405px">
    <svg viewBox="0 0 32 32"><path d="M16 0 32 16 16 32 0 16Z" fill="#555"/><path d="M12 11c1 6 4 9 9 10l1.5-2.5-2.5-1.5-1.5 1.3c-1.8-.9-3-2.2-3.8-4l1.3-1.5-1.5-2.5Z" fill="#fff"/></svg>
    <span>555-014-2739</span>
  </div>
  <div class="contact" style="left:580px">
    <svg viewBox="0 0 32 32"><path d="M16 0 32 16 16 32 0 16Z" fill="#111"/><g fill="none" stroke="#fff" stroke-width="1.1"><circle cx="16" cy="16" r="5.5"/><ellipse cx="16" cy="16" rx="2.3" ry="5.5"/><path d="M10.5 16h11"/></g></svg>
    <span>torlensystems.example</span>
  </div>
</section>

<section class="card card-back">
  <div class="back-texture" role="img" aria-label="Soft white flowing wave texture background"></div>
  <div class="back-brand"><span class="name">TORLEN</span><span class="sub">SYSTEMS</span></div>
  <p class="service-list">ACCESS CONTROL | CCTV | INTRUSION ALARM | AUDIO-VISUAL | FIRE | DATA</p>
  <div class="tagline-band"><h2>YOUR SECURITY AND<br>TECHNOLOGY PARTNER</h2></div>
  <div class="address-box">ADDRESS</div>
</section>

</body>
</html>
```